New Business Card

We need to refresh our business cards. We designed these ourselves and we have no graphic design experience. We would like to find a new business card design that is professional and unique. We are an auto finance company. Feel free to play with the logo, but we would like to keep the eye very present on the card. Our corporate colors are green, grey, and white.
Green - RGB - 168,215,27; HEX - #AADD22
Grey - RGB - 196,196,196; HEX - #C4C4C4
Updates
Need to upload the vector file to finalize the project. The last logo was for a jpeg that didn't stretch well.
Industry/Entity Type
Financial Service
Contact Information for Business Card
Honestly don't know...I need your help!

```html
<!DOCTYPE html>
<html lang="en">
<head>
<meta charset="utf-8">
<title>Keenway Capital — Business Card</title>
<link href="https://fonts.googleapis.com/css2?family=Fira+Sans:wght@500;600&family=Montserrat:ital,wght@1,300&display=swap" rel="stylesheet">
<style>
  :root {
    --green: #a9cf3b;
    --green-deep: #6cbc46;
    --green-text: #a5cd39;
    --grey: #c4c4c4;
    --grey-sub: #a9a9a9;
    --grey-text: #7a7a7a;
    --white: #ffffff;
  }
  html, body {
    margin: 0;
    width: 1200px;
    height: 1200px;
    overflow: hidden;
    background: var(--white);
  }
  .canvas { position: relative; width: 1200px; height: 1200px; }
  .card {
    position: absolute;
    width: 678px;
    height: 440px;
    overflow: hidden;
  }
  .card svg.card-bg { position: absolute; inset: 0; width: 100%; height: 100%; }

  /* Front */
  .card-front { left: 262px; top: 125px; }
  .front-mark {
    position: absolute;
    left: 294px; top: 124px;
    width: 90px; height: 90px;
    border-radius: 50%;
    background: var(--white);
  }
  .front-wordmark {
    position: absolute;
    left: 0; right: 0; top: 236px;
    text-align: center;
    font-family: "Fira Sans", sans-serif;
    font-weight: 500;
    color: var(--white);
  }
  .front-wordmark .name-main { display: block; font-size: 50px; line-height: 1.1; letter-spacing: -0.5px; }
  .front-wordmark .name-sub { display: block; font-size: 16px; letter-spacing: 0.95em; margin-top: 10px; padding-left: 0.95em; }

  /* Back */
  .card-back {
    left: 260px; top: 616px;
    background: var(--white);
    box-shadow: -6px 10px 22px rgba(0,0,0,0.12);
  }
  .back-mark {
    position: absolute;
    left: 114px; top: 64px;
    width: 64px; height: 64px;
    border-radius: 50%;
    background: var(--green-text);
  }
  .back-wordmark {
    position: absolute;
    left: 214px; top: 76px;
    font-family: "Fira Sans", sans-serif;
    font-weight: 500;
    color: var(--green-text);
  }
  .back-wordmark .name-main { display: block; font-size: 37px; line-height: 1; letter-spacing: -0.4px; }
  .back-wordmark .name-sub { display: block; font-size: 12px; letter-spacing: 1.05em; margin-top: 6px; padding-left: 12px; color: var(--grey-sub); }

  .contact {
    position: absolute;
    left: 96px; top: 180px;
    font-family: "Montserrat", sans-serif;
    font-style: italic;
    font-weight: 300;
    color: var(--grey-text);
  }
  .person-name {
    margin: 0;
    font-family: "Fira Sans", sans-serif;
    font-style: normal;
    font-weight: 500;
    font-size: 29px;
    color: var(--green-text);
    line-height: 1.1;
  }
  .person-role { margin: 4px 0 0; font-size: 16px; letter-spacing: 0.2px; }
  .person-phone { margin: 30px 0 0; font-size: 16px; }
  .person-email { margin: 5px 0 0; font-size: 16px; }
  .website { position: absolute; left: 96px; top: 366px; margin: 0; font-family: "Montserrat", sans-serif; font-style: italic; font-weight: 300; font-size: 16px; color: var(--grey-text); }
</style>
</head>
<body>
<div class="canvas">

  <section class="card card-front" aria-label="Card front">
    <svg class="card-bg" viewBox="0 0 848 550" preserveAspectRatio="none" aria-hidden="true">
      <defs>
        <linearGradient id="sweep" x1="0" y1="0" x2="1" y2="0">
          <stop offset="0" stop-color="#6cbc46"/>
          <stop offset="0.35" stop-color="#8bc541"/>
          <stop offset="0.65" stop-color="#a9cf3b"/>
          <stop offset="1" stop-color="#a9cf3b"/>
        </linearGradient>
        <linearGradient id="corner" x1="0" y1="0" x2="1" y2="0">
          <stop offset="0" stop-color="#a9cf3b"/>
          <stop offset="1" stop-color="#6cbc46"/>
        </linearGradient>
      </defs>
      <rect width="848" height="550" fill="var(--green)"/>
      <path d="M0 292 C120 130 300 40 470 0 H848 V255 C720 420 560 510 430 550 H0 Z" fill="url(#sweep)"/>
      <path d="M848 255 C740 400 600 490 430 550 H848 Z" fill="url(#corner)"/>
    </svg>
    <span class="front-mark" aria-hidden="true"></span>
    <div class="front-wordmark">
      <span class="name-main">Keenway</span>
      <span class="name-sub">CAPITAL</span>
    </div>
  </section>

  <section class="card card-back" aria-label="Card back">
    <svg class="card-bg" viewBox="0 0 848 550" preserveAspectRatio="none" aria-hidden="true">
      <defs>
        <linearGradient id="silver" x1="0" y1="0" x2="0" y2="1">
          <stop offset="0" stop-color="#c8c9cb"/>
          <stop offset="0.6" stop-color="#d9dadb"/>
          <stop offset="1" stop-color="#ffffff"/>
        </linearGradient>
        <linearGradient id="leaf" x1="0" y1="0" x2="0" y2="1">
          <stop offset="0" stop-color="#a5cd39"/>
          <stop offset="1" stop-color="#93c63d"/>
        </linearGradient>
      </defs>
      <path d="M782 0 H802 C826 230 770 400 665 550 H605 C720 400 808 230 782 0 Z" fill="url(#silver)"/>
      <path d="M802 0 H848 V550 H665 C770 400 826 230 802 0 Z" fill="url(#leaf)"/>
    </svg>
    <span class="back-mark" aria-hidden="true"></span>
    <div class="back-wordmark">
      <span class="name-main">Keenway</span>
      <span class="name-sub">CAPITAL</span>
    </div>
    <div class="contact">
      <p class="person-name">First Last Name</p>
      <p class="person-role">BUSINESS ROLE</p>
      <p class="person-phone">0000 123 456</p>
      <p class="person-email">name@email.com</p>
    </div>
    <p class="website">www.website.com</p>
  </section>

</div>
</body>
</html>
```